Ferris Contracting LLC Business Card Design

I am looking for a creative and unique business card design. We are a commercial construction general contractor. With the name "FERRIS" Contracting, I am hoping to see some neat designs that correlate with the name.

```html
<!DOCTYPE html>
<html lang="en">
<head>
<meta charset="utf-8">
<title>Ferris Contracting LLC – Business Card</title>
<link rel="stylesheet" href="https://fonts.googleapis.com/css2?family=Montserrat:wght@400;500;700&family=Roboto:wght@400&display=swap">
<style>
  :root {
    --backdrop: #c4c4c4;
    --card: #0b0c0e;
    --brand-blue: #29a9e0;
    --ink-light: #f2f2f2;
  }
  * { margin: 0; padding: 0; box-sizing: border-box; }
  html, body {
    width: 1200px;
    height: 1200px;
    overflow: hidden;
    background: var(--backdrop);
  }
  .canvas {
    position: relative;
    width: 1200px;
    height: 1200px;
  }
  .card {
    position: absolute;
    left: 239px;
    width: 722px;
    height: 410px;
    background: var(--card);
    border-radius: 24px;
  }
  .card--front { top: 150px; }
  .card--back { top: 645px; }

  .identity {
    position: absolute;
    left: 62px;
    top: 58px;
    display: flex;
    align-items: center;
    font-family: "Montserrat", sans-serif;
    white-space: nowrap;
  }
  .identity__name {
    color: var(--brand-blue);
    font-weight: 700;
    font-size: 24px;
    letter-spacing: 0.2px;
  }
  .identity__divider {
    display: inline-block;
    width: 3px;
    height: 18px;
    background: var(--ink-light);
    margin: 0 13px 0 15px;
  }
  .identity__role {
    color: var(--ink-light);
    font-weight: 400;
    font-size: 19px;
  }

  .address {
    position: absolute;
    left: 62px;
    top: 200px;
    font-family: "Roboto", Arial, sans-serif;
    color: #ffffff;
    font-size: 19.5px;
    line-height: 26px;
  }

  .contacts {
    position: absolute;
    left: 62px;
    top: 272px;
    list-style: none;
    font-family: "Montserrat", sans-serif;
    color: var(--ink-light);
    font-size: 19.5px;
  }
  .contacts__item {
    display: flex;
    align-items: center;
    height: 27px;
  }
  .contacts__icon {
    width: 16px;
    height: 16px;
    margin-right: 9px;
    flex: none;
  }

  .wordmark {
    position: absolute;
    font-family: "Montserrat", sans-serif;
    font-weight: 700;
    color: var(--brand-blue);
    text-align: center;
    line-height: 1.15;
    white-space: nowrap;
  }
  .wordmark--small {
    left: 448px;
    top: 256px;
    width: 230px;
    font-size: 22px;
    letter-spacing: 2px;
  }
  .wordmark--large {
    left: 0;
    top: 0;
    width: 722px;
    height: 410px;
    display: flex;
    flex-direction: column;
    justify-content: center;
    font-size: 44px;
    letter-spacing: 4px;
  }
</style>
</head>
<body>
<main class="canvas">
  <section class="card card--front">
    <div class="identity">
      <span class="identity__name">MARK ELLISON</span>
      <span class="identity__divider"></span>
      <span class="identity__role">Manager</span>
    </div>

    <address class="address" style="font-style:normal">
      Harlow Road Suite 210<br>
      Oakdale, TN 37829
    </address>

    <ul class="contacts">
      <li class="contacts__item">
        <svg class="contacts__icon" viewBox="0 0 16 16" aria-hidden="true">
          <path fill="#29a9e0" d="M3.2 1.5l2.2 2.6-1.2 1.6c.9 2 2.3 3.4 4.3 4.3l1.6-1.2 2.6 2.2-1.2 2.2C7 13.2 2.8 9 1 4.4z"/>
          <path fill="none" stroke="#29a9e0" stroke-width="1.2" d="M9.5 3.2a3.5 3.5 0 0 1 3.3 3.3M9.5 .8a6 6 0 0 1 5.7 5.7"/>
        </svg>
        (555) 214-6038
      </li>
      <li class="contacts__item">
        <svg class="contacts__icon" viewBox="0 0 16 16" aria-hidden="true">
          <rect x="0.5" y="3" width="15" height="11" rx="1" fill="#29a9e0"/>
          <path d="M1 3.8l7 5 7-5" fill="none" stroke="#0b0c0e" stroke-width="1.3"/>
        </svg>
        mark@ferriscontractingllc.com
      </li>
      <li class="contacts__item">
        <svg class="contacts__icon" viewBox="0 0 16 16" aria-hidden="true">
          <circle cx="8" cy="8" r="7.5" fill="#29a9e0"/>
          <path fill="#0b0c0e" d="M4 4.5c1.5-.5 2.5.5 2.2 1.8-.3 1-1.6 1.2-1.4 2.6.2 1-.8 1.4-1.6.6C2.5 8.7 2.6 5.4 4 4.5zM9.5 9c1-.4 2.6.2 2.5 1.4-.1 1.3-1.6 2.6-2.4 2-.6-.5.4-1.6-.3-2.2-.5-.5-.4-1 .2-1.2zM9 2.8c1 .1 2 .6 2.6 1.3-.6.4-1.6.2-2-.3-.3-.3-.9-.4-.6-1z"/>
        </svg>
        www.ferriscontractingllc.com
      </li>
    </ul>

    <div class="wordmark wordmark--small">FERRIS<br>CONTRACTING</div>
  </section>

  <section class="card card--back">
    <div class="wordmark wordmark--large">
      <span>FERRIS</span>
      <span>CONTRACTING</span>
    </div>
  </section>
</main>
</body>
</html>
```